Lueur de Provins Immerse in the enchanting flavors of France at Lueur de Provins

A menu that is French in style with the Eiffel Tower. A elegant menu that is in rich blue with red or gold trimmings, we are a French Bakey and Cafe

Target Market(s)

30 to 55 people

Industry/Entity Type

Restaurant

Font styles to use
Decorative

Colors
0054AA
0677BA
7BADD7
CADEEF
E8F1F8
EB3D1F
EC4F4E
F09395
F8D3D4
FCEDEE

Requirements
Must have
• the attachment "My Brunch Specials" is the Menu I want you to create, it has all the text, "My Brunch Special Complete" is a word version. The menu size should be 4 1/4 wide by 14 inches long 2 Sided. must have our logo at the top , Make the font larger, because our biggest complaint about our menu is it is hard to read
Nice to have
• I would love to incorporate the Eiffel Tower as a silhouette in the background
Should not have
• I do not want too many pictures or small print

```html
<!DOCTYPE html>
<html lang="en">
<head>
<meta charset="utf-8">
<title>Lueur de Provins — Brunch &amp; Drink Menu</title>
<link rel="stylesheet" href="https://fonts.googleapis.com/css2?family=Oswald:wght@300;400&family=Roboto:wght@400;500;700&display=swap">
<style>
  :root {
    --navy: #13284d;
    --navy-deep: #0d1e3b;
    --red: #c9413b;
    --red-soft: #d4524a;
    --white: #ffffff;
    --ink: #13284d;
    --page: #ffffff;
  }
  * { box-sizing: border-box; margin: 0; padding: 0; }
  html, body { width: 1200px; height: 2721px; overflow: hidden; background: var(--page); }
  body { font-family: "Roboto", Arial, sans-serif; position: relative; }

  .brand-header {
    position: absolute; top: 150px; left: 0; width: 1200px;
    display: flex; align-items: center; justify-content: center; gap: 22px;
  }
  .brand-dot { width: 26px; height: 26px; border-radius: 50%; background: var(--red); }
  .brand-name {
    font-family: "Roboto", sans-serif; font-weight: 500; font-size: 44px;
    letter-spacing: 2px; color: var(--ink);
  }

  .menu-spread {
    position: absolute; top: 420px; left: 40px; width: 1120px; height: 2200px;
    display: flex; justify-content: space-between;
  }
  .menu-panel {
    width: 540px; height: 2200px; background: var(--navy); color: var(--white);
    display: flex; flex-direction: column; position: relative; overflow: hidden;
  }

  .panel-hero {
    height: 330px; background: linear-gradient(180deg, #c9413b 0%, #bb3c38 100%);
    border-bottom: 5px solid var(--white);
    border-radius: 0 0 50% 50% / 0 0 26% 26%;
    margin: 0 -40px; display: flex; align-items: flex-end; justify-content: center;
    padding-bottom: 70px;
  }
  .panel-name {
    font-family: "Roboto", sans-serif; font-weight: 500; font-size: 26px;
    letter-spacing: 1px; color: var(--white);
  }

  .section-title {
    font-family: "Oswald", sans-serif; font-weight: 300; text-align: center;
    letter-spacing: 3px; text-transform: uppercase;
  }
  .brunch .section-title { font-size: 32px; color: var(--white); margin: 26px 0 10px; }
  .drinks .section-title { font-size: 34px; color: var(--red-soft); margin: 22px 0 6px; }
  .drinks .section-title.latte { margin-top: 12px; }

  .menu-list { flex: 1; display: flex; flex-direction: column; justify-content: space-around; padding: 0 44px; }
  .menu-item { text-align: center; }
  .item-title {
    position: relative; display: inline-block; background: var(--red);
    font-weight: 700; font-size: 19px; padding: 6px 30px; margin-bottom: 12px;
    min-width: 280px; color: var(--white);
  }
  .item-title::before, .item-title::after {
    content: ""; position: absolute; top: 50%; width: 14px; height: 3px; background: var(--red);
  }
  .item-title::before { left: -20px; }
  .item-title::after { right: -20px; }
  .item-desc { font-size: 13.5px; line-height: 1.55; font-weight: 500; }

  .panel-scene {
    height: 150px; background: linear-gradient(180deg, var(--navy) 0%, var(--navy-deep) 100%);
  }
  .panel-footer {
    height: 170px; background: var(--red); display: flex; align-items: flex-end;
    justify-content: center; padding-bottom: 28px; margin-top: 10px;
  }
</style>
</head>
<body>
  <header class="brand-header">
    <span class="brand-dot" aria-hidden="true"></span>
    <span class="brand-name">Lueur de Provins</span>
  </header>

  <main class="menu-spread">
    <section class="menu-panel brunch">
      <div class="panel-hero" role="img" aria-label="Red-tinted photograph of a Paris landmark behind the restaurant name">
        <span class="panel-name">Lueur de Provins</span>
      </div>
      <h2 class="section-title">Brunch Specials</h2>
      <div class="menu-list">
        <article class="menu-item">
          <h3 class="item-title">Ratatouille &amp; eggs $18</h3>
          <p class="item-desc">Experience the essence of Provence with our Ratatouille, a vibrant medley of roasted squash, peppers, tomatoes, eggplant, infused with fragrant fresh herbs. Served with two perfectly poached eggs, and your choice of flavorful andouille sausage or crispy bacon. Accompanied by a side of crusty baguette. It's a hearty dish that celebrates the flavors of the Mediterranean countryside.</p>
        </article>
        <article class="menu-item">
          <h3 class="item-title">Le Grande Breakfast $15</h3>
          <p class="item-desc">Start your day in style with our Le Grande Breakfast, a feast fit for royalty. Customize your morning indulgence with two eggs cooked to your preference, paired with either savory bacon or succulent chicken sausage. Choose between a freshly baked baguette or a buttery croissant to accompany your meal. Complete your breakfast by selecting from an array of sides including crispy hash browns, savory roasted potatoes, or a refreshing fruit salad. Bon appetit!</p>
        </article>
        <article class="menu-item">
          <h3 class="item-title">Smoked Salmon Tartine $14</h3>
          <p class="item-desc">Delight in the luxurious flavors of our Smoked Salmon Tartine, a culinary masterpiece that elevates breakfast to new heights. Indulge in truffled scrambled eggs nestled atop smoked salmon, adorned with tangy pickled red onions, briny caper berries, crisp cucumber, juicy tomato, and peppery arugula. All artfully arranged on multigrain bread generously spread with herb-infused cream cheese.</p>
        </article>
        <article class="menu-item">
          <h3 class="item-title">Le Benedict Salmon $14</h3>
          <p class="item-desc">Savor the classic elegance of Eggs Benedict, featuring two perfectly poached eggs nestled on toasted English muffins, with luscious smoked salmon and ripe tomato slices crowned with a velvety lemon-infused Hollandaise sauce. A timeless brunch delight crafted to perfection.</p>
        </article>
        <article class="menu-item">
          <h3 class="item-title">Salmon Atlantique $14</h3>
          <p class="item-desc">Enjoy a bed of crisp mixed greens adorned with delicate smoked salmon, sweet golden raisins, creamy goat cheese, and crunchy walnuts. All dressed in a tantalizing balsamic vinaigrettethat ties the elements together perfectly.</p>
        </article>
        <article class="menu-item">
          <h3 class="item-title">Beef Bourguignon $18</h3>
          <p class="item-desc">Indulge in our rich and comforting flavors of savory, tender beef slowly braised in red wine, creating a luscious sauce that envelops pearl onions, carrots, and mushrooms in a symphony of flavors. Served alongside buttered egg noodles. It's a hearty and soul-warming meal that promises pure culinary bliss.</p>
        </article>
        <article class="menu-item">
          <h3 class="item-title">Tourte au Poulet $15</h3>
          <p class="item-desc">Discover the indulgent flavors of our Tourte au Poulet, a savory delight that marries tender marinated chicken with the richness of Swiss cheese and the sweetness of onions, all encased in layers of flaky pastry. Topped with a savory mushroom medley and decadent bechamel sauce. A true comfort classic to delight your senses.</p>
        </article>
      </div>
      <div class="panel-scene" role="img" aria-label="Faint navy photograph of a Paris skyline along the bottom edge"></div>
    </section>

    <section class="menu-panel drinks">
      <h2 class="section-title">Drink Specials</h2>
      <div class="menu-list">
        <article class="menu-item">
          <h3 class="item-title">Bottomless Mimosa $18</h3>
          <p class="item-desc">Embark on an endless journey of delight with our Bottomless Mimosa, featuring Hollowell champagne, infusing each sip with a sparkling sensation. Tailor your experience with your preferred flavor profile - opt for the timeless twist of classic orange juice or tangy cranberry juice for a refreshing zing. Continuously poured to ensure your glass is always full.</p>
        </article>
        <article class="menu-item">
          <h3 class="item-title">Apple Cider-Mimosa $9</h3>
          <p class="item-desc">A delightful twist on the classic mimosa. Crafted with champagne and crisp apple cider. To elevate the experience, we adorn the glass with a caramel rim dipped in brown sugar, adding a touch of indulgent sweetness to every sip.</p>
        </article>
        <article class="menu-item">
          <h3 class="item-title">Blood Orange or Pineapple Spritz $12</h3>
          <p class="item-desc">Introducing our vibrant spritz cocktail, a tantalizing blend of Tobin. Blend &amp; premium Vestrova Vodka, sweet vermouth, and a touch of sweetness from a carefully muddled sugar cube. This effervescent libation reaches new heights with the addition of bubbly Clairsource, your choice of either Blood Orange or Pineapple syrup injects a burst of fruity allure into every sip.</p>
        </article>
        <article class="menu-item">
          <h3 class="item-title">Peach Bellini $9</h3>
          <p class="item-desc">Try our perfectly balanced Peach Bellini with each sip you capture the crispness of champagne with the irresistible sweetness of peach. It's a sublime fusion of sophistication and sweetness.</p>
        </article>
        <article class="menu-item">
          <h3 class="item-title">Espresso Martini $10</h3>
          <p class="item-desc">Our Espresso Martini is a decadent blend of bold espresso, rich chocolate martini,and luxurious Bellamonte chocolate syrup. It's the ultimate indulgence for coffee and chocolate lovers alike.</p>
        </article>
        <article class="menu-item">
          <h3 class="item-title">Kir Royale $10</h3>
          <p class="item-desc">Our Kir Royale is a delightful fusion of the crisp, sparkling champagne bubbles and the sweet sophistication of black currant. a luxurious and indulgent drink that's perfect for any occasion.</p>
        </article>
        <h2 class="section-title latte">Latte</h2>
        <article class="menu-item">
          <h3 class="item-title">Truffle Latte $6</h3>
          <p class="item-desc">We start with rich Bellamonte chocolate, known for its velvety smoothness and intense flavor. Then, we add a drizzle of salted caramel, adding a perfect balance of sweetness and a hint of savory richness. Finally, we combine this delightful blend with perfectly steamed milk to create a creamy and indulgent latte that will satisfy even the most discerning palate.</p>
        </article>
        <article class="menu-item">
          <h3 class="item-title">Napoleon Latte $6</h3>
          <p class="item-desc">We start with rich Bellamonte chocolate, known for its velvety smoothness and intense flavor. Then, we add a drizzle of salted caramel, adding a perfect balance of sweetness and a hint of savory richness. Finally, we combine this delightful blend with perfectly steamed milk to create a creamy and indulgent latte that will satisfy even the most discerning palate.</p>
        </article>
        <article class="menu-item">
          <h3 class="item-title">Chai Latte $6</h3>
          <p class="item-desc">Our robust chai tea concentrate, infused with a symphony of cinnamon, cardamom, cloves, and ginger, sets the stage for a journey of aromatic delight. Paired with velvety steamed milk, each sip offers a harmonious blend of bold spices and creamy richness. Topped with a sprinkle of cinnamon, it's the perfect finishing touch to this comforting treat.</p>
        </article>
      </div>
      <div class="panel-footer" role="img" aria-label="Red-tinted photograph of a Paris landmark behind the restaurant name">
        <span class="panel-name">Lueur de Provins</span>
      </div>
    </section>
  </main>
</body>
</html>
```